Summer Drinks Flyer for Coffee Shop

We are a coffee shop in London and would like to have a cool and nice flyer for our summer drinks (juices and frozen drink) flyer - see on the attached file for the list

Attached you can find an "attempt" - please note that I would no necessary need the image below.

I also attache our new logo.

thank you

```html
<!DOCTYPE html>
<html lang="en">
<head>
<meta charset="utf-8">
<title>Sunleaf Café – new summer drinks menu</title>
<link rel="stylesheet" href="https://fonts.googleapis.com/css2?family=Comfortaa:wght@300;400&family=Libre+Bodoni:wght@400&display=swap">
<style>
  :root {
    --page-bg: #ecebe7;
    --paper: #ffffff;
    --lime: #a9cf2e;
    --lime-deep: #93bf1c;
    --lime-pale: #e3f0b4;
    --leaf-glow: #6c9d3a;
    --olive: #8d8a4d;
    --juice-ink: #4f6b1f;
    --frozen-ink: #d4472a;
    --coffee-ink: #6a4519;
    --price-juice: #6f7f4a;
    --price-frozen: #c9563a;
    --price-coffee: #7a5a35;
    --brand-ink: #5d7d22;
    --accent-new: #ec7a2a;
    --accent-line: #8bbf22;
    --ring: rgba(255,255,255,0.9);
  }
  html, body {
    margin: 0;
    width: 1200px;
    height: 1000px;
    overflow: hidden;
    background: var(--page-bg);
  }
  .flyer {
    position: absolute;
    left: 290px;
    top: 60px;
    width: 620px;
    height: 880px;
    overflow: hidden;
    background:
      linear-gradient(180deg,
        var(--paper) 0%,
        var(--paper) 36%,
        var(--lime-pale) 44%,
        var(--lime) 56%,
        var(--lime-deep) 66%,
        var(--lime) 74%,
        var(--lime-pale) 80%,
        var(--paper) 86%,
        var(--paper) 100%);
    box-shadow: 0 6px 18px rgba(0,0,0,0.18);
    font-family: "Comfortaa", sans-serif;
  }
  .hero-splash {
    position: absolute;
    left: 0;
    top: 0;
    width: 620px;
    height: 320px;
    background:
      radial-gradient(ellipse 42% 30% at 48% 28%, rgba(240,120,40,0.75), transparent 70%),
      radial-gradient(ellipse 30% 22% at 36% 58%, rgba(200,30,90,0.55), transparent 70%),
      radial-gradient(ellipse 30% 24% at 72% 44%, rgba(160,190,60,0.55), transparent 70%),
      radial-gradient(ellipse 55% 40% at 50% 30%, rgba(169,207,46,0.45), transparent 80%),
      linear-gradient(180deg, var(--lime) 0%, var(--lime-pale) 50%, var(--paper) 100%);
  }
  .rings {
    position: absolute;
    left: 0;
    top: 0;
  }
  .menu-block {
    position: absolute;
    text-align: center;
    line-height: 1.2;
  }
  .menu-title { font-size: 21px; font-weight: 400; margin: 0 0 4px; }
  .menu-items { font-size: 13.5px; font-weight: 300; margin: 0; padding: 0; list-style: none; }
  .menu-price { font-family: "Libre Bodoni", serif; font-size: 27px; margin-top: 10px; }
  .juices { left: 176px; top: 305px; width: 250px; color: var(--juice-ink); }
  .juices .menu-price { color: var(--price-juice); }
  .frozen { left: 40px; top: 505px; width: 270px; color: var(--frozen-ink); }
  .frozen .menu-price { color: var(--price-frozen); }
  .coffees { left: 330px; top: 490px; width: 230px; color: var(--coffee-ink); }
  .coffees .menu-price { color: var(--price-coffee); }
  .coffees .menu-items, .frozen .menu-items { font-size: 14px; }
  .extra-note {
    position: absolute;
    margin: 0;
    text-align: center;
    color: #fff;
    font-size: 14px;
    font-weight: 300;
    line-height: 1.2;
  }
  .note-mint { left: 80px; top: 376px; width: 100px; }
  .note-syrup { left: 458px; top: 379px; width: 94px; }
  .brand-block {
    position: absolute;
    left: 0;
    top: 740px;
    width: 620px;
    text-align: center;
  }
  .brand-name {
    font-size: 34px;
    font-weight: 300;
    color: var(--brand-ink);
    line-height: 1;
  }
  .tagline {
    margin-top: 16px;
    font-size: 19px;
    font-weight: 400;
    color: var(--accent-line);
  }
  .tagline .tag-new { color: var(--accent-new); }
</style>
</head>
<body>
  <main class="flyer">
    <div class="hero-splash" role="img" aria-label="Photo of tipped glasses splashing orange, green, red and pink fruit juices"></div>

    <svg class="rings" width="620" height="880" viewBox="0 0 620 880" aria-hidden="true">
      <defs>
        <radialGradient id="mintGlow">
          <stop offset="0" stop-color="#6c9d3a" stop-opacity="0.95"/>
          <stop offset="0.8" stop-color="#6c9d3a" stop-opacity="0.6"/>
          <stop offset="1" stop-color="#6c9d3a" stop-opacity="0"/>
        </radialGradient>
        <radialGradient id="syrupGlow">
          <stop offset="0" stop-color="#8d8a4d" stop-opacity="1"/>
          <stop offset="0.8" stop-color="#8d8a4d" stop-opacity="0.75"/>
          <stop offset="1" stop-color="#8d8a4d" stop-opacity="0"/>
        </radialGradient>
      </defs>
      <circle cx="130" cy="395" r="72" fill="url(#mintGlow)"/>
      <circle cx="505" cy="397" r="66" fill="url(#syrupGlow)"/>
      <g fill="none" stroke="var(--ring)" stroke-width="2.5">
        <circle cx="130" cy="395" r="55"/>
        <circle cx="505" cy="397" r="52"/>
        <circle cx="301" cy="385" r="125"/>
        <circle cx="175" cy="580" r="135"/>
        <circle cx="445" cy="570" r="135"/>
      </g>
    </svg>

    <p class="extra-note note-mint">add mint<br>or ginger<br>for free</p>
    <p class="extra-note note-syrup">add syrup<br>shot for<br>10p</p>

    <section class="menu-block juices">
      <h2 class="menu-title">fruit juices</h2>
      <ul class="menu-items">
        <li>orange and carrot</li>
        <li>orange and pineapple</li>
        <li>pineapple and apple</li>
        <li>apple and kiwi</li>
        <li>carrot and ginger</li>
      </ul>
      <div class="menu-price">£2.95</div>
    </section>

    <section class="menu-block frozen">
      <h2 class="menu-title">frozen<br>fruit drinks</h2>
      <ul class="menu-items">
        <li>strawberry and banana</li>
        <li>pineapple, mango and banana</li>
      </ul>
      <div class="menu-price">£2.95</div>
    </section>

    <section class="menu-block coffees">
      <h2 class="menu-title">iced coffees</h2>
      <ul class="menu-items">
        <li>iced coffee</li>
        <li>iced latte</li>
        <li>iced chocolate drink</li>
      </ul>
      <div class="menu-price">£2.45</div>
    </section>

    <footer class="brand-block">
      <div class="brand-name">Sunleaf Café</div>
      <div class="tagline"><span class="tag-new">new</span> summer drinks menu</div>
    </footer>
  </main>
</body>
</html>
```